Brindlewood Holdings LLC - Business Cards

Need the following information on the cards:

Name: Marcus T Velding
Title: Chief Executive Manager

Business address:
412 N Pickerel Ridge Road #118
Fernmoor, Il 60917

Phone: (555) 481-0362 - Business
BRX FFL license number: 5-81-xxx-xx-xx-04519
Email: marcus.velding@brindlewoodholdingsffl.example

Target Market(s)

Firearm owners

Industry/Entity Type

Firearms industry,

Contact Information for Business Card

Contact number, name and title, web page address, email, business address and brx license number,

Requirements
Must have
• Name, title, business address, phone numbers, BRX license numbers, web page address and email address.
Nice to have
• Cellphone number,

```html
<!DOCTYPE html>
<html lang="en">
<head>
<meta charset="utf-8">
<title>Brindlewood Holdings LLC – Business Cards</title>
<link rel="stylesheet" href="https://fonts.googleapis.com/css2?family=Montserrat:wght@600;700&family=Open+Sans:wght@400;600&display=swap">
<style>
  :root {
    --brand-red: #cc1b23;
    --deep-red: #a8141b;
    --ink: #231f20;
    --paper: #ffffff;
    --backdrop: #cfcfcf;
    --line-dark: #2b2b2b;
  }
  * { margin: 0; padding: 0; box-sizing: border-box; }
  html, body { width: 1200px; height: 800px; overflow: hidden; }
  body {
    background: var(--backdrop);
    font-family: "Open Sans", Arial, sans-serif;
    position: relative;
  }
  .card {
    position: absolute;
    left: 285px;
    width: 630px;
    height: 360px;
    border-radius: 22px;
    overflow: hidden;
  }
  .card--front { top: 22px; background: var(--paper); border: 3px solid var(--brand-red); }
  .card--back { top: 418px; background: var(--brand-red); }

  .card__art { position: absolute; inset: 0; width: 100%; height: 100%; }

  .holder { position: absolute; left: 42px; top: 52px; }
  .holder__name {
    font-family: "Montserrat", Arial, sans-serif;
    font-weight: 700; font-size: 30px; letter-spacing: 1px;
    color: var(--brand-red); text-transform: uppercase; line-height: 1.1;
  }
  .holder__title {
    font-family: "Montserrat", Arial, sans-serif;
    font-weight: 700; font-size: 15px; letter-spacing: 1px;
    color: var(--ink); text-transform: uppercase; margin-top: 4px;
  }

  .contact-list {
    position: absolute; left: 42px; top: 158px;
    list-style: none; color: var(--paper); font-size: 13px; line-height: 22px;
  }
  .contact-list li { display: flex; align-items: center; gap: 10px; white-space: nowrap; }
  .contact-list svg { width: 15px; height: 15px; flex: none; }

  .address {
    position: absolute; left: 42px; top: 270px;
    font-size: 17px; line-height: 24px; color: var(--ink); font-style: normal;
  }

  .brand-mark {
    position: absolute; left: 402px; top: 52px; width: 190px; height: 190px;
    border: 3px solid var(--line-dark); border-radius: 50%; background: var(--paper);
    display: flex; flex-direction: column; align-items: center; justify-content: center;
  }
  .brand-mark__name {
    font-family: "Montserrat", Arial, sans-serif; font-weight: 700;
    color: var(--brand-red); text-align: center; font-size: 19px; line-height: 1.25; letter-spacing: 1px;
  }

  .licence { position: absolute; left: 402px; top: 268px; font-size: 16px; line-height: 22px; }
  .licence__label { color: var(--brand-red); }
  .licence__number { color: var(--ink); }

  .brand-mark--embossed {
    left: 205px; top: 70px; width: 220px; height: 220px;
    background: transparent; border: 3px solid var(--deep-red);
  }
  .brand-mark--embossed .brand-mark__name { color: var(--deep-red); font-size: 23px; }
</style>
</head>
<body>

<section class="card card--front" aria-label="Business card front">
  <svg class="card__art" viewBox="0 0 624 354" aria-hidden="true">
    <polygon points="505,0 624,0 624,120 580,120" fill="#cc1b23"/>
    <polygon points="0,148 430,148 395,252 0,252" fill="#231f20"/>
  </svg>

  <div class="holder">
    <h1 class="holder__name">Marcus T Velding</h1>
    <p class="holder__title">Chief Executive Manager</p>
  </div>

  <ul class="contact-list">
    <li><svg viewBox="0 0 16 16"><path d="M4 1l3 3-2 2c1 2 3 4 5 5l2-2 3 3-2 3C7 15 1 9 1 3z" fill="#cc1b23"/></svg>(555) 481-0362</li>
    <li><svg viewBox="0 0 16 16"><rect x="4" y="1" width="8" height="14" rx="1.5" fill="none" stroke="#ffffff" stroke-width="1.5"/><circle cx="8" cy="12.5" r="0.9" fill="#ffffff"/></svg>(555) 481-0362</li>
    <li><svg viewBox="0 0 16 16"><rect x="1" y="3" width="14" height="10" fill="#cc1b23"/><path d="M1 3l7 6 7-6" fill="none" stroke="#ffffff" stroke-width="1.2"/></svg>marcus.velding@brindlewoodholdingsffl.example</li>
    <li><svg viewBox="0 0 16 16"><circle cx="8" cy="8" r="7" fill="#cc1b23"/><path d="M1 8h14M8 1c-3 4-3 10 0 14M8 1c3 4 3 10 0 14" fill="none" stroke="#ffffff" stroke-width="1"/></svg>www.brindlewoodholdingsffl.example</li>
  </ul>

  <address class="address">
    412 N Pickerel Ridge Road #118<br>
    Fernmoor, Il 60917
  </address>

  <div class="brand-mark">
    <p class="brand-mark__name">BRINDLEWOOD<br>HOLDINGS LLC</p>
  </div>

  <p class="licence">
    <span class="licence__label">BRX FFL License No</span><br>
    <span class="licence__number">5-81-xxx-xx-xx-04519</span>
  </p>
</section>

<section class="card card--back" aria-label="Business card back">
  <div class="brand-mark brand-mark--embossed">
    <p class="brand-mark__name">BRINDLEWOOD<br>HOLDINGS LLC</p>
  </div>
</section>

</body>
</html>
```